Speaker and Author Website

I need a website to promote myself as a public speaker and a site where I can promote my books. I would like to have a website similar to this page

http://brentolvane.example/

The categories I would be covering on my site are the following:

Motivation, Leadership, Technology, Small Business, Inspiration

I want a wordpress site, so it is easy for me to make changes when needed. I need a blog site within my site to.

```html
<!DOCTYPE html>
<html lang="en">
<head>
<meta charset="utf-8">
<title>Dana Morell — Speaker and Author</title>
<link rel="stylesheet" href="https://fonts.googleapis.com/css2?family=Archivo:wght@600;700;800&family=Arimo:wght@400;700&display=swap">
<style>
:root{
  --navy:#13143a;
  --band:#7a7a7a;
  --panel:#f4f4f4;
  --tagline:#c9c9c9;
  --ink:#222;
  --muted:#8a8a8a;
  --link:#3a7fc4;
  --rule:#dcdcdc;
  --red:#c8342f;
  --photo-warm:#b85a4a;
  --photo-dark:#3a2320;
}
*{box-sizing:border-box;margin:0;padding:0}
html,body{width:1054px;height:1200px;overflow:hidden;background:#fff}
body{position:relative;font-family:"Arimo",Arial,sans-serif;color:var(--ink)}
.abs{position:absolute}
.topbar{left:0;top:0;width:1054px;height:47px;background:var(--navy)}
.topnav{left:314px;top:15px;display:flex;font-size:13px;color:#e8e8f0}
.topnav span{padding:0 10px;border-left:1px solid #555a80;line-height:18px}
.topnav span:first-child{border-left:0;padding-left:0;color:#aaaabb}
.search{left:750px;top:11px;width:212px;height:25px;background:#fff;border-radius:3px}
.search svg{position:absolute;right:6px;top:4px}
.header{left:91px;top:71px;width:873px;height:186px;background:var(--panel)}
.portrait{left:111px;top:16px;width:183px;height:197px;border:3px solid #fff;box-shadow:0 1px 4px rgba(0,0,0,.35);background:linear-gradient(160deg,#6a5555 0%,#b04a48 45%,#e06a66 70%,#7a3030 100%)}
.name{left:120px;top:224px;font-family:"Archivo",Arial,sans-serif;font-weight:800;font-size:24px;letter-spacing:.5px;color:#444}
.name b{color:var(--navy);font-weight:800}
.tagline{left:300px;top:120px;width:666px;text-align:center;font-family:"Archivo",Arial,sans-serif;font-weight:800;font-size:23px;line-height:28px;color:var(--tagline)}
.catbar{left:91px;top:258px;width:873px;height:45px;background:var(--band);display:flex}
.catbar span{display:flex;align-items:center;justify-content:center;font-family:"Archivo",Arial,sans-serif;font-weight:800;font-size:20px;color:#f2f2f2;border-right:1px solid #999}
.catbar span:last-child{border-right:0}
.catbar .current{color:var(--navy)}
.sec-title{font-family:"Archivo",Arial,sans-serif;font-weight:600;font-size:16px;color:#333;letter-spacing:.3px}
.frame{border:1px solid var(--rule);padding:5px;background:#fff}
.feature-photo{left:95px;top:373px;width:182px;height:258px}
.feature-photo div{width:100%;height:100%;background:linear-gradient(150deg,#5a4a48 0%,#c05050 40%,#e8706a 60%,#d8d0c8 90%)}
.feature-text{left:287px;top:371px;width:190px}
.feature-text h3{font-weight:400;font-size:11.5px;color:#111;margin-bottom:17px}
.feature-text p{font-size:11.5px;line-height:19px;color:var(--muted)}
.more-btn{left:288px;top:573px;width:61px;height:30px;border:1px solid #d5d5d5;border-radius:3px;font-size:11px;font-weight:700;display:flex;align-items:center;justify-content:center;color:#333}
.links-box{left:490px;top:322px;width:224px;height:304px;border:1px solid var(--rule);padding:30px 10px 0 10px}
.links-box h2{margin-bottom:18px}
.links-box li{list-style:none;font-size:11.5px;color:var(--muted);height:32px;display:flex;align-items:center;border-bottom:1px solid #e6e6e6}
.links-box li:last-child{border-bottom:0}
.links-box li::before{content:"";width:9px;height:9px;background:#ddd;margin-right:11px;flex:none}
.news-item{left:734px;width:230px;display:flex}
.news-thumb{width:55px;height:55px;border:1px solid var(--rule);padding:3px;flex:none}
.news-thumb div{width:100%;height:100%;background:linear-gradient(180deg,#e8eef2,#8aa0b8 70%,#6a6e78)}
.news-text{margin-left:19px;font-size:11.5px;line-height:19px;color:var(--muted)}
.news-text b{color:var(--link)}
.post-title{left:101px;top:660px;font-weight:700;font-size:18.5px;color:#111}
.post-rule{left:95px;top:683px;width:506px;height:4px;background:#d6d6d6}
.share-row{left:102px;top:698px;display:flex;align-items:center;font-size:11px}
.btn{height:20px;padding:0 7px;display:flex;align-items:center;gap:5px;color:#fff;font-weight:700;border-radius:2px}
.btn i{width:8px;height:8px;background:#fff;display:block}
.count{height:20px;padding:0 6px;border:1px solid #ccc;border-radius:2px;display:flex;align-items:center;color:#777;margin:0 14px 0 4px}
.send{display:flex;align-items:center;gap:6px;color:#555}
.send i{width:18px;height:18px;background:#3cb521;border-radius:3px;display:block}
.hero{left:95px;top:728px;width:501px;height:327px;border:1px solid #ccc;background:radial-gradient(ellipse at 50% 40%,#b8242a 0%,#6a2418 30%,#3a2418 60%,#140d0c 100%)}
.excerpt{left:95px;top:1070px;width:506px;font-size:12.2px;line-height:14.6px;color:#777}
.meta{left:95px;top:1138px;width:506px;display:flex;font-size:10px;color:#666;align-items:baseline}
.meta span{margin-right:20px}
.meta a{color:#111;text-decoration:underline}
.read{color:#111;text-decoration:underline;font-size:13px}
.meta .read{margin-left:auto}
.side-band{left:641px;width:323px;height:31px;background:var(--band);color:#fff;font-weight:700;font-size:19px;padding-left:8px;display:flex;align-items:center}
.book{left:641px;top:691px;width:95px;height:142px;background:linear-gradient(170deg,#2e3e6a 0%,#3a3a50 40%,#c8342f 75%,#8a1f1c 100%)}
.author-text{left:741px;top:690px;width:222px;font-size:11.2px;line-height:14.5px;color:#666}
.side-read{right:90px}
.side-rule{left:641px;width:323px;height:2px;background:#666}
.latest{left:641px;width:323px;display:flex}
.latest-thumb{width:57px;height:57px;border:1px solid #ddd;padding:2px;flex:none;margin-left:2px}
.latest-thumb div{width:100%;height:100%;background:linear-gradient(150deg,#5a4a48 0%,#c04848 45%,#e86a66 70%,#7a3030 100%)}
.latest-text{margin-left:10px;width:250px}
.latest-text h4{font-size:13px;font-weight:700;color:#111;line-height:15px}
.latest-text p{font-size:11.2px;line-height:14.5px;color:#888}
.latest-text .read{display:block;text-align:right;margin-top:3px}
.footer-band{left:0;top:1193px;width:1054px;height:7px;background:#333}
</style>
</head>
<body>
<div class="abs topbar"></div>
<nav class="abs topnav"><span>Home</span><span>About</span><span>Speaking</span><span>Recommended Books</span><span>Contact</span></nav>
<div class="abs search"><svg width="20" height="18" viewBox="0 0 20 18"><circle cx="8" cy="8" r="6" fill="none" stroke="#ccc" stroke-width="2.5"/><line x1="12.5" y1="12.5" x2="18" y2="17" stroke="#ccc" stroke-width="3"/></svg></div>

<header>
  <div class="abs header"></div>
  <div class="abs portrait" role="img" aria-label="Portrait of Dana Morell speaking into a microphone"></div>
  <div class="abs name">DANA <b>MORELL</b></div>
  <p class="abs tagline">Award Winning Technology Consultant, Entrepreneur,<br>Small Business Leader, and Motivational Speaker</p>
</header>

<nav class="abs catbar">
  <span class="current" style="width:159px">Technology</span>
  <span style="width:151px">Leadership</span>
  <span style="width:143px">Motivation</span>
  <span style="width:197px">Small Business</span>
  <span style="width:223px">Entrepreneurship</span>
</nav>

<h2 class="abs sec-title" style="left:95px;top:322px">GOOD IDEAS FOR YOUR BUSINESS</h2>
<div class="abs frame feature-photo"><div role="img" aria-label="Dana Morell holding her book at an event"></div></div>
<div class="abs feature-text">
  <h3>SMALL ENTERPRISE BUREAU</h3>
  <p>Dana and her company has been seen on Channel 8 News Bayview, Small Enterprise Bureau (SEB) publication, Bayview Business Journal, Pacific Voices Media, Bayview Courier, and Bayview Metro Magazine.</p>
</div>
<div class="abs more-btn">MORE</div>

<section class="abs links-box">
  <h2 class="sec-title">USEFUL LINKS</h2>
  <ul>
    <li>Aipisicing eli sed do eiusmod</li>
    <li>Rempdunt et labore et dolore</li>
    <li>Magna aliqua etder enim ad</li>
    <li>Minim veniam quis nostrud</li>
    <li>Exercitation des ullamcaboris</li>
    <li>Nisi ut aliquip massa dolore</li>
    <li>Ea commodo consequatuis</li>
  </ul>
</section>

<h2 class="abs sec-title" style="left:734px;top:322px">OUR NEWS</h2>
<div class="abs news-item" style="top:370px"><div class="news-thumb"><div role="img" aria-label="Businessman at a desk"></div></div><div class="news-text">Lorem ipsum dolor sit amet,<br>consectetur adipiscing...<br><b>March 14, 2013</b></div></div>
<div class="abs news-item" style="top:469px"><div class="news-thumb"><div role="img" aria-label="Businessman in a shirt and tie"></div></div><div class="news-text">Lorem ipsum dolor sit amet,<br>consectetur adipiscing...<br><b>March 5, 2013</b></div></div>
<div class="abs news-item" style="top:568px"><div class="news-thumb"><div role="img" aria-label="Businessman in a grey suit"></div></div><div class="news-text">Lorem ipsum dolor sit amet,<br>consectetur adipiscing...<br><b>February 14, 2013</b></div></div>

<article>
  <h1 class="abs post-title">Lorem Ipsum is simply dummy text</h1>
  <div class="abs post-rule"></div>
  <div class="abs share-row">
    <span class="btn" style="background:#3b5b98"><i></i>Share</span><span class="count">472</span>
    <span class="btn" style="background:#3a8fc8"><i></i>Post</span><span class="count">17</span>
    <span class="btn" style="background:#fff;color:var(--red);border:1px solid #ccc">Like</span><span class="count">4</span>
    <span class="btn" style="background:var(--red)">Save</span><span class="count">9</span>
    <span class="send"><i></i>Send This</span>
  </div>
  <div class="abs hero" role="img" aria-label="Conference hall with audience facing a red-curtained stage and screens"></div>
  <p class="abs excerpt">Lorem Ipsum is simply dummy text of the printing and typesetting industry. Lorem Ipsum has been the industry's standard dummy text ever since the 1500s, when an unknown printer took a galley of type and scrambled it to make a type specimen book. It has survived not only five centuries, but also the leap into electronic typesetting, remaining essentially unchanged...</p>
  <div class="abs meta"><span>Posted In <a>Technology</a></span><span>Posted by <a>admin</a></span><span>Post type <b style="color:#111;font-weight:400">Image</b></span><a class="read">Read More →</a></div>
</article>

<aside>
  <div class="abs side-band" style="top:654px">Authour</div>
  <div class="abs book" role="img" aria-label="Cover of the Steady Climb Guide book"></div>
  <p class="abs author-text">Best-Selling Author, Dana Morell and her company NetCore Partners, Inc., is considered one of the top Information Technology service and solutions provider in the country. Dana Morell was inducted into the National Circle of Best-Selling Authors and was presented with a Quill Mark Award in September 2013 for her contribution to the Best-Selling Book "Steady Climb Guide." ...</p>
  <a class="abs read side-read" style="top:822px">Read More →</a>
  <div class="abs side-rule" style="top:845px"></div>

  <div class="abs side-band" style="top:857px">Latest Post</div>
  <div class="abs latest" style="top:895px"><div class="latest-thumb"><div role="img" aria-label="Dana Morell holding her book"></div></div><div class="latest-text"><h4>Lorem Ipsum is simply</h4><p>Lorem Ipsum is simplyLorem Ipsum is simply Lorem Ipsum is simply Lorem Ipsum is simply ...</p><a class="read">Read More →</a></div></div>
  <div class="abs side-rule" style="top:967px;height:1px;background:#888"></div>
  <div class="abs latest" style="top:975px"><div class="latest-thumb"><div role="img" aria-label="Dana Morell holding her book"></div></div><div class="latest-text"><h4>Lorem Ipsum is simply</h4><p>Lorem Ipsum is simplyLorem Ipsum is simply Lorem Ipsum is simply Lorem Ipsum is simply ...</p><a class="read">Read More →</a></div></div>
  <div class="abs side-rule" style="top:1048px;height:1px;background:#888"></div>
  <div class="abs latest" style="top:1056px"><div class="latest-thumb"><div role="img" aria-label="Dana Morell holding her book"></div></div><div class="latest-text"><h4>Lorem Ipsum is simply</h4><p>Lorem Ipsum is simplyLorem Ipsum is simply Lorem Ipsum is simply Lorem Ipsum is simply ...</p><a class="read">Read More →</a></div></div>
  <div class="abs side-rule" style="top:1128px;height:1px;background:#888"></div>
  <div class="abs latest" style="top:1136px"><div class="latest-thumb"><div role="img" aria-label="Dana Morell holding her book"></div></div><div class="latest-text"><h4>Lorem Ipsum is simply</h4><p>Lorem Ipsum is simplyLorem Ipsum is simply Lorem Ipsum is simply Lorem Ipsum is simply ...</p></div></div>
</aside>

<div class="abs footer-band"></div>
</body>
</html>
```